Album Cover for upcoming release

Hi, I need an album cover for a song that I’ll be releasing soon. The album cover must contain the title of the song, which is:

Carry the Tide (remix)

The album cover must also contain the artist name:

Derek Hanmore

The song is a remix of a song that I released in late-May called “Carry the Tide.” I wrote the original song for my wife. If you’re interested, please give it a listen on Tunevault or Soundmarrow under the artist Derek Hanmore. Here’s a Soundmarrow link to the original song (it already has more than 175,000 streams):

https://play.soundmarrow.example/track/7RtZpLc92XGb4nHqWmEsVd?si=kd3TfPzX8wQmLr2NbYcVhe

The remix is VERY, VERY different! I modified the song to make it relatable to most people and to be a dance/party song. Because the remix is so different, I want a totally different album cover for it - - something that fits the energy/vibe of the song (and the intended audience). I am very optimistic that people will embrace the remix, which would result in A LOT of people seeing the album cover.

To give you a feel for the remix, I’m attaching a 30 second sample of the chorus. Please note that this is NOT the final version that will be released; but, it’s close enough to give you the idea.

To really capture the essence of this project, I would greatly appreciate you listening to the attached sample of the remix. Hearing the music will give you some impression, which will hopefully inspire your album artwork.

Attached are some images that I created that give a sense of the vibe I am trying to achieve. Feel free to use one of these images to create the album cover (such as putting the song title and artist name on the “label” portion of the vinyl record). But, you are NOT required to use one os these images.
Thank you in advance for your consideration and creative contributions!

Target Market(s)

Dance and party crowd; night clubs, sporting events, weddings

Font styles to use
Sans Serif

Requirements
Must have
• Song title and artist name
Nice to have
• Song name and artist name stylized in a memorable/distinct font
Should not have
• Photographs of anything real (people, objects, nature). Animated can be fine

```html
<!DOCTYPE html>
<html lang="en">
<head>
<meta charset="utf-8">
<title>Carry the Tide (remix) – Derek Hanmore</title>
<link rel="stylesheet" href="https://fonts.googleapis.com/css2?family=Bungee&family=Bungee+Shade&family=Arimo:wght@700&display=swap">
<style>
  :root {
    --backdrop: #d0d2ce;
    --sky-gold: #e2b845;
    --sky-amber: #d58c45;
    --wave-violet: #6a4a9c;
    --wave-blue: #2f4f9e;
    --wave-teal: #1a9a9c;
    --wave-green: #22ab94;
    --wave-pink: #e0507a;
    --sand-orange: #d0873e;
    --ink: #141414;
    --ring: rgba(255, 255, 255, 0.85);
    --vinyl: #0c0c0c;
    --groove: #2a2a2a;
    --label-rim: #d9b93a;
  }
  * { margin: 0; padding: 0; box-sizing: border-box; }
  html, body {
    width: 1200px;
    height: 850px;
    overflow: hidden;
    background: var(--backdrop);
  }
  .canvas {
    position: relative;
    width: 1200px;
    height: 850px;
  }
  .record {
    position: absolute;
    left: 533px;
    top: 115px;
    width: 630px;
    height: 630px;
  }
  .record-label {
    position: absolute;
    left: 744px;
    top: 326px;
    width: 208px;
    height: 208px;
    border-radius: 50%;
    border: 5px solid var(--label-rim);
    background: radial-gradient(circle at 50% 50%, var(--wave-green) 0%, var(--wave-teal) 35%, var(--wave-blue) 60%, var(--wave-pink) 85%, var(--sand-orange) 100%);
    display: flex;
    flex-direction: column;
    align-items: center;
    justify-content: center;
    gap: 4px;
    text-align: center;
    font-family: "Bungee", sans-serif;
    color: var(--ink);
  }
  .label-title { font-size: 14px; line-height: 1; }
  .label-subtitle { font-size: 12px; line-height: 1; }
  .label-artist { font-size: 15px; line-height: 1; margin-top: 6px; }
  .cover {
    position: absolute;
    left: 45px;
    top: 100px;
    width: 650px;
    height: 650px;
    overflow: hidden;
    border-radius: 4px;
  }
  .cover-artwork {
    position: absolute;
    inset: 0;
    background:
      radial-gradient(ellipse 60% 35% at 95% 20%, rgba(201, 70, 40, 0.75), transparent 70%),
      radial-gradient(ellipse 55% 30% at 90% 90%, rgba(190, 70, 30, 0.7), transparent 70%),
      linear-gradient(180deg,
        var(--sky-gold) 0%,
        var(--sky-amber) 22%,
        #e8a468 30%,
        var(--wave-violet) 38%,
        var(--wave-blue) 44%,
        var(--wave-teal) 54%,
        var(--wave-green) 64%,
        var(--wave-blue) 76%,
        var(--wave-pink) 84%,
        var(--sand-orange) 92%,
        var(--sky-gold) 100%);
  }
  .cover-ring {
    position: absolute;
    left: 0;
    top: 0;
    width: 650px;
    height: 650px;
    pointer-events: none;
  }
  .title {
    position: absolute;
    left: 88px;
    top: 258px;
    font-family: "Bungee Shade", sans-serif;
    font-size: 58px;
    font-weight: 400;
    line-height: 1.12;
    color: var(--ink);
    letter-spacing: 1px;
    white-space: nowrap;
  }
  .title-line { display: block; }
  .subtitle {
    position: absolute;
    left: 151px;
    top: 465px;
    font-family: "Bungee Shade", sans-serif;
    font-size: 39px;
    color: var(--ink);
    letter-spacing: 1px;
  }
  .credits {
    position: absolute;
    left: 43px;
    top: 597px;
    font-family: "Arimo", sans-serif;
    font-weight: 700;
    font-size: 9px;
    line-height: 1.25;
    color: var(--ink);
  }
</style>
</head>
<body>
  <main class="canvas">
    <svg class="record" viewBox="0 0 630 630" aria-hidden="true">
      <circle cx="315" cy="315" r="313" fill="var(--vinyl)"/>
      <g fill="none" stroke="var(--groove)" stroke-width="1.5">
        <circle cx="315" cy="315" r="290"/>
        <circle cx="315" cy="315" r="262"/>
        <circle cx="315" cy="315" r="236"/>
        <circle cx="315" cy="315" r="206"/>
        <circle cx="315" cy="315" r="178"/>
        <circle cx="315" cy="315" r="150"/>
        <circle cx="315" cy="315" r="124"/>
      </g>
    </svg>
    <div class="record-label" role="img" aria-label="Record label with the cover's wave artwork in teal, blue and pink">
      <span class="label-title">Carry the Tide</span>
      <span class="label-subtitle">Remix</span>
      <span class="label-artist">Derek Hanmore</span>
    </div>
    <section class="cover">
      <div class="cover-artwork" role="img" aria-label="Illustrated sunset beach: golden sky with streaked clouds, a large setting sun, flowing blue, teal and pink waves, and silhouetted palm trees with glowing lights"></div>
      <svg class="cover-ring" viewBox="0 0 650 650" aria-hidden="true">
        <circle cx="228" cy="341" r="96" fill="none" stroke="var(--ring)" stroke-width="2"/>
      </svg>
      <h1 class="title">
        <span class="title-line">Carry</span>
        <span class="title-line">the Tide</span>
      </h1>
      <p class="subtitle">Remix</p>
      <p class="credits">Lorem ipsum dolor sit amet, consectetuer adipiscing<br>elit, sed diam nonummy nibh euismod tincidunt ut</p>
    </section>
  </main>
</body>
</html>
```